Calendar design with baby pictures

I need to get 2 calendars designed, one wall hanging A5 size and one table top. I want to use my baby pics on it in very creative way. On some months i just want to use one picture and on some i will want to use a collage of few pics. The design should allow me to place pictures myself later on as i dont want to upload so many pics here.

Baby

```html
<!DOCTYPE html>
<html lang="en">
<head>
<meta charset="utf-8">
<title>Baby Calendar 2015</title>
<link rel="stylesheet" href="https://fonts.googleapis.com/css2?family=Fredoka:wght@600&family=Gochi+Hand&family=Nunito:wght@600&family=Cormorant+Garamond:wght@500&family=Lora:ital,wght@1,700&display=swap">
<style>
:root{
  --bg:#ffffff;
  --ink:#3a3a3a;
  --weekend:#e0197a;
  --muted:#b4b4b4;
  --cover-blue:#2f9be0;
  --jan:#6f96cf; --jan-tint:#c3d0ee;
  --feb:#4fa3d8; --feb-tint:#bfe0f3;
  --mar:#a6d65a; --mar-tint:#dcefc0;
  --apr:#3fb8a0; --apr-tint:#bfe6dc;
  --may:#e8a59c; --may-tint:#f6d8d3;
  --jun:#e070b0; --jun-tint:#f5c8e0;
  --jul:#f0a070; --jul-tint:#fad8c0;
  --aug:#f2c040; --aug-tint:#fbe7b0;
  --sep:#d8193e; --sep-tint:#f3b9c4;
  --oct:#a07a88; --oct-tint:#e2d3d8;
  --nov:#7a78c0; --nov-tint:#d5d4ee;
  --dec:#b07ac0; --dec-tint:#e3cdea;
}
*{box-sizing:border-box;margin:0;padding:0}
html,body{width:1200px;height:999px;overflow:hidden;background:var(--bg)}
.board{position:relative;width:1200px;height:999px}

.page{position:absolute;width:36.8em;height:49.5em;background:#fff;
  box-shadow:.35em .45em .7em rgba(0,0,0,.45);display:flex;flex-direction:column;overflow:hidden}
.m-jan{--theme:var(--jan);--tint:var(--jan-tint)}
.m-feb{--theme:var(--feb);--tint:var(--feb-tint)}
.m-mar{--theme:var(--mar);--tint:var(--mar-tint)}
.m-apr{--theme:var(--apr);--tint:var(--apr-tint)}
.m-may{--theme:var(--may);--tint:var(--may-tint)}
.m-jun{--theme:var(--jun);--tint:var(--jun-tint)}
.m-jul{--theme:var(--jul);--tint:var(--jul-tint)}
.m-aug{--theme:var(--aug);--tint:var(--aug-tint)}
.m-sep{--theme:var(--sep);--tint:var(--sep-tint)}
.m-oct{--theme:var(--oct);--tint:var(--oct-tint)}
.m-nov{--theme:var(--nov);--tint:var(--nov-tint)}
.m-dec{--theme:var(--dec);--tint:var(--dec-tint)}

.month-title{height:5.2em;flex:none;background:var(--theme);border-bottom:.3em dotted #fff;
  display:flex;align-items:center;justify-content:flex-end;padding-right:1em;
  font-family:"Fredoka",sans-serif;font-weight:600;font-size:1em;color:#fff;white-space:nowrap}
.month-title span{font-size:2.7em;letter-spacing:.02em}

.photo{flex:1;min-height:0;display:grid;gap:.4em;background:#fff}
.photo div{width:100%;height:100%}
.collage-3{grid-template-columns:1fr 1fr;grid-template-rows:1fr 1fr}
.collage-3 div:first-child{grid-row:1 / 3}
.collage-4{grid-template-columns:1fr 1fr;grid-template-rows:1fr 1fr}

.calendar{height:14.6em;flex:none;padding:.6em 1.2em .6em;
  background:linear-gradient(var(--tint),#fff 85%);display:flex;flex-direction:column;gap:.45em}
.weekdays,.days{display:grid;grid-template-columns:repeat(7,1fr);column-gap:.6em}
.weekdays{flex:none;height:2em}
.weekdays span{background:var(--theme);opacity:.85;border-radius:50%;height:2em;
  display:flex;align-items:center;justify-content:center;color:#fff;
  font-family:"Gochi Hand",cursive;font-size:1em;line-height:1}
.weekdays span b{font-weight:400;font-size:1.5em}
.days{flex:1;min-height:0;grid-auto-rows:minmax(0,1fr);row-gap:.35em}
.days span{background:#fff;border-radius:50%;box-shadow:0 .15em .2em rgba(0,0,0,.25);
  display:flex;align-items:center;justify-content:center;line-height:1;min-height:0;
  font-family:"Nunito",sans-serif;font-weight:600;color:var(--ink);font-size:1.45em}
.days span:nth-child(7n+6),.days span:nth-child(7n){color:var(--weekend)}
.days span.out{color:var(--muted)}

.cover{left:45px;top:17px;width:288px;height:525px;font-size:10px;display:block;
  background:radial-gradient(ellipse at 55% 45%,#f3e6d4 0%,#e9d3a8 40%,#d9b560 100%)}
.cover .photo-fill{position:absolute;inset:0}
.year-digits{position:absolute;left:20px;top:33px;display:flex;flex-direction:column;gap:15px}
.year-digits span{width:85px;height:60px;border-radius:50%;
  background:radial-gradient(ellipse at 40% 35%,#7fd0f5,#2f9be0 70%,#1b7fc4);
  display:flex;align-items:center;justify-content:center;
  font-family:"Cormorant Garamond",serif;font-weight:500;font-size:62px;color:#fff;line-height:1;
  font-variant-numeric:lining-nums}
.dedication{position:absolute;right:14px;bottom:14px;text-align:right;
  font-family:"Lora",serif;font-style:italic;font-weight:700;font-size:15px;line-height:1.3;color:var(--cover-blue)}

.feature-jan{left:440px;top:20px;font-size:10px}
.feature-dec{left:815px;top:30px;font-size:9.4px;height:52.5em;transform:rotate(-4deg)}
.feature-dec .calendar{height:15.6em}

.thumbs{position:absolute;left:107px;top:557px;display:grid;
  grid-template-columns:repeat(6,140px);grid-template-rows:repeat(2,198px);column-gap:38px;row-gap:28px}
.thumbs .page{position:relative;font-size:3.8px;width:140px;height:198px}
.thumbs .calendar{height:16em}
</style>
</head>
<body>
<main class="board">

  <section class="page cover">
    <div class="photo-fill" role="img" aria-label="Cover photo of the baby smiling on a white fur rug"></div>
    <div class="year-digits"><span>2</span><span>0</span><span>1</span><span>5</span></div>
    <p class="dedication">Specially for you with love.<br>From Milo</p>
  </section>

  <article class="page m-jan feature-jan">
    <h2 class="month-title"><span>January 2015</span></h2>
    <div class="photo"><div role="img" aria-label="January photo of the baby lying on a blue blanket" style="background:linear-gradient(160deg,#b9cde6,#e8cdb8 55%,#d8b49a)"></div></div>
    <div class="calendar">
      <div class="weekdays"><span><b>Mo</b></span><span><b>Tu</b></span><span><b>We</b></span><span><b>Th</b></span><span><b>Fr</b></span><span><b>Sa</b></span><span><b>Su</b></span></div>
      <div class="days"><span class="out">29</span><span class="out">30</span><span class="out">31</span><span>1</span><span>2</span><span>3</span><span>4</span><span>5</span><span>6</span><span>7</span><span>8</span><span>9</span><span>10</span><span>11</span><span>12</span><span>13</span><span>14</span><span>15</span><span>16</span><span>17</span><span>18</span><span>19</span><span>20</span><span>21</span><span>22</span><span>23</span><span>24</span><span>25</span><span>26</span><span>27</span><span>28</span><span>29</span><span>30</span><span>31</span><span class="out">1</span></div>
    </div>
  </article>

  <article class="page m-dec feature-dec">
    <h2 class="month-title"><span>December 2015</span></h2>
    <div class="photo"><div role="img" aria-label="December photo of the baby on a wooden rocking horse by a Christmas tree" style="background:linear-gradient(120deg,#2f3a2a,#6a5a48 45%,#c9a070 70%,#d8d0c8)"></div></div>
    <div class="calendar">
      <div class="weekdays"><span><b>Mo</b></span><span><b>Tu</b></span><span><b>We</b></span><span><b>Th</b></span><span><b>Fr</b></span><span><b>Sa</b></span><span><b>Su</b></span></div>
      <div class="days"><span class="out">30</span><span>1</span><span>2</span><span>3</span><span>4</span><span>5</span><span>6</span><span>7</span><span>8</span><span>9</span><span>10</span><span>11</span><span>12</span><span>13</span><span>14</span><span>15</span><span>16</span><span>17</span><span>18</span><span>19</span><span>20</span><span>21</span><span>22</span><span>23</span><span>24</span><span>25</span><span>26</span><span>27</span><span>28</span><span>29</span><span>30</span><span>31</span><span class="out">1</span><span class="out">2</span><span class="out">3</span></div>
    </div>
  </article>

  <section class="thumbs">
    <article class="page m-jan">
      <h3 class="month-title"><span>January 2015</span></h3>
      <div class="photo"><div role="img" aria-label="January photo" style="background:linear-gradient(160deg,#b9cde6,#e8cdb8 55%,#d8b49a)"></div></div>
      <div class="calendar"><div class="weekdays"><span><b>Mo</b></span><span><b>Tu</b></span><span><b>We</b></span><span><b>Th</b></span><span><b>Fr</b></span><span><b>Sa</b></span><span><b>Su</b></span></div>
      <div class="days"><span class="out">29</span><span class="out">30</span><span class="out">31</span><span>1</span><span>2</span><span>3</span><span>4</span><span>5</span><span>6</span><span>7</span><span>8</span><span>9</span><span>10</span><span>11</span><span>12</span><span>13</span><span>14</span><span>15</span><span>16</span><span>17</span><span>18</span><span>19</span><span>20</span><span>21</span><span>22</span><span>23</span><span>24</span><span>25</span><span>26</span><span>27</span><span>28</span><span>29</span><span>30</span><span>31</span><span class="out">1</span></div></div>
    </article>

    <article class="page m-feb">
      <h3 class="month-title"><span>February 2015</span></h3>
      <div class="photo"><div role="img" aria-label="February photo of the baby in a blue shirt" style="background:linear-gradient(160deg,#2a2a2a,#6b5a50 50%,#8aa6c8)"></div></div>
      <div class="calendar"><div class="weekdays"><span><b>Mo</b></span><span><b>Tu</b></span><span><b>We</b></span><span><b>Th</b></span><span><b>Fr</b></span><span><b>Sa</b></span><span><b>Su</b></span></div>
      <div class="days"><span class="out">26</span><span class="out">27</span><span class="out">28</span><span class="out">29</span><span class="out">30</span><span class="out">31</span><span>1</span><span>2</span><span>3</span><span>4</span><span>5</span><span>6</span><span>7</span><span>8</span><span>9</span><span>10</span><span>11</span><span>12</span><span>13</span><span>14</span><span>15</span><span>16</span><span>17</span><span>18</span><span>19</span><span>20</span><span>21</span><span>22</span><span>23</span><span>24</span><span>25</span><span>26</span><span>27</span><span>28</span><span class="out">1</span></div></div>
    </article>

    <article class="page m-mar">
      <h3 class="month-title"><span>March 2015</span></h3>
      <div class="photo collage-3"><div role="img" aria-label="March collage photo, baby sitting" style="background:linear-gradient(#e8dcc8,#c8a880)"></div><div role="img" aria-label="March collage photo, close-up" style="background:linear-gradient(#c8b8a8,#d8b090)"></div><div role="img" aria-label="March collage photo, baby in a white shirt" style="background:linear-gradient(#7a6a60,#e0d8d0)"></div></div>
      <div class="calendar"><div class="weekdays"><span><b>Mo</b></span><span><b>Tu</b></span><span><b>We</b></span><span><b>Th</b></span><span><b>Fr</b></span><span><b>Sa</b></span><span><b>Su</b></span></div>
      <div class="days"><span class="out">23</span><span class="out">24</span><span class="out">25</span><span class="out">26</span><span class="out">27</span><span class="out">28</span><span>1</span><span>2</span><span>3</span><span>4</span><span>5</span><span>6</span><span>7</span><span>8</span><span>9</span><span>10</span><span>11</span><span>12</span><span>13</span><span>14</span><span>15</span><span>16</span><span>17</span><span>18</span><span>19</span><span>20</span><span>21</span><span>22</span><span>23</span><span>24</span><span>25</span><span>26</span><span>27</span><span>28</span><span>29</span><span>30</span><span>31</span><span class="out">1</span><span class="out">2</span><span class="out">3</span><span class="out">4</span><span class="out">5</span></div></div>
    </article>

    <article class="page m-apr">
      <h3 class="month-title"><span>April 2015</span></h3>
      <div class="photo"><div role="img" aria-label="April photo of the baby sitting" style="background:linear-gradient(160deg,#4a3a30,#a07a60 50%,#e0c0a0)"></div></div>
      <div class="calendar"><div class="weekdays"><span><b>Mo</b></span><span><b>Tu</b></span><span><b>We</b></span><span><b>Th</b></span><span><b>Fr</b></span><span><b>Sa</b></span><span><b>Su</b></span></div>
      <div class="days"><span class="out">30</span><span class="out">31</span><span>1</span><span>2</span><span>3</span><span>4</span><span>5</span><span>6</span><span>7</span><span>8</span><span>9</span><span>10</span><span>11</span><span>12</span><span>13</span><span>14</span><span>15</span><span>16</span><span>17</span><span>18</span><span>19</span><span>20</span><span>21</span><span>22</span><span>23</span><span>24</span><span>25</span><span>26</span><span>27</span><span>28</span><span>29</span><span>30</span><span class="out">1</span><span class="out">2</span><span class="out">3</span></div></div>
    </article>

    <article class="page m-may">
      <h3 class="month-title"><span>May 2015</span></h3>
      <div class="photo"><div role="img" aria-label="May photo of the baby in a pink shirt" style="background:linear-gradient(160deg,#b8a890,#e0b8a0 50%,#d87068)"></div></div>
      <div class="calendar"><div class="weekdays"><span><b>Mo</b></span><span><b>Tu</b></span><span><b>We</b></span><span><b>Th</b></span><span><b>Fr</b></span><span><b>Sa</b></span><span><b>Su</b></span></div>
      <div class="days"><span class="out">27</span><span class="out">28</span><span class="out">29</span><span class="out">30</span><span>1</span><span>2</span><span>3</span><span>4</span><span>5</span><span>6</span><span>7</span><span>8</span><span>9</span><span>10</span><span>11</span><span>12</span><span>13</span><span>14</span><span>15</span><span>16</span><span>17</span><span>18</span><span>19</span><span>20</span><span>21</span><span>22</span><span>23</span><span>24</span><span>25</span><span>26</span><span>27</span><span>28</span><span>29</span><span>30</span><span>31</span></div></div>
    </article>

    <article class="page m-jun">
      <h3 class="month-title"><span>June 2015</span></h3>
      <div class="photo collage-4"><div role="img" aria-label="June collage photo one" style="background:linear-gradient(#c8c0b8,#a89080)"></div><div role="img" aria-label="June collage photo two" style="background:linear-gradient(#e0d8d0,#c0a898)"></div><div role="img" aria-label="June collage photo three" style="background:linear-gradient(#8a7a68,#c8a048)"></div><div role="img" aria-label="June collage photo four" style="background:linear-gradient(#6a80b8,#e0d8d0)"></div></div>
      <div class="calendar"><div class="weekdays"><span><b>Mo</b></span><span><b>Tu</b></span><span><b>We</b></span><span><b>Th</b></span><span><b>Fr</b></span><span><b>Sa</b></span><span><b>Su</b></span></div>
      <div class="days"><span>1</span><span>2</span><span>3</span><span>4</span><span>5</span><span>6</span><span>7</span><span>8</span><span>9</span><span>10</span><span>11</span><span>12</span><span>13</span><span>14</span><span>15</span><span>16</span><span>17</span><span>18</span><span>19</span><span>20</span><span>21</span><span>22</span><span>23</span><span>24</span><span>25</span><span>26</span><span>27</span><span>28</span><span>29</span><span>30</span><span class="out">1</span><span class="out">2</span><span class="out">3</span><span class="out">4</span><span class="out">5</span></div></div>
    </article>

    <article class="page m-jul">
      <h3 class="month-title"><span>July 2015</span></h3>
      <div class="photo"><div role="img" aria-label="July photo of the baby in a white shirt" style="background:linear-gradient(160deg,#e8e4e0,#d0c8c0 50%,#8a90a0)"></div></div>
      <div class="calendar"><div class="weekdays"><span><b>Mo</b></span><span><b>Tu</b></span><span><b>We</b></span><span><b>Th</b></span><span><b>Fr</b></span><span><b>Sa</b></span><span><b>Su</b></span></div>
      <div class="days"><span class="out">29</span><span class="out">30</span><span>1</span><span>2</span><span>3</span><span>4</span><span>5</span><span>6</span><span>7</span><span>8</span><span>9</span><span>10</span><span>11</span><span>12</span><span>13</span><span>14</span><span>15</span><span>16</span><span>17</span><span>18</span><span>19</span><span>20</span><span>21</span><span>22</span><span>23</span><span>24</span><span>25</span><span>26</span><span>27</span><span>28</span><span>29</span><span>30</span><span>31</span><span class="out">1</span><span class="out">2</span></div></div>
    </article>

    <article class="page m-aug">
      <h3 class="month-title"><span>August 2015</span></h3>
      <div class="photo"><div role="img" aria-label="August photo of the baby with a football" style="background:linear-gradient(160deg,#3a302a,#6a5a4a 50%,#e0e0e0)"></div></div>
      <div class="calendar"><div class="weekdays"><span><b>Mo</b></span><span><b>Tu</b></span><span><b>We</b></span><span><b>Th</b></span><span><b>Fr</b></span><span><b>Sa</b></span><span><b>Su</b></span></div>
      <div class="days"><span class="out">27</span><span class="out">28</span><span class="out">29</span><span class="out">30</span><span class="out">31</span><span>1</span><span>2</span><span>3</span><span>4</span><span>5</span><span>6</span><span>7</span><span>8</span><span>9</span><span>10</span><span>11</span><span>12</span><span>13</span><span>14</span><span>15</span><span>16</span><span>17</span><span>18</span><span>19</span><span>20</span><span>21</span><span>22</span><span>23</span><span>24</span><span>25</span><span>26</span><span>27</span><span>28</span><span>29</span><span>30</span><span>31</span><span class="out">1</span><span class="out">2</span><span class="out">3</span><span class="out">4</span><span class="out">5</span><span class="out">6</span></div></div>
    </article>

    <article class="page m-sep">
      <h3 class="month-title"><span>September 2015</span></h3>
      <div class="photo"><div role="img" aria-label="September photo of the baby in a green shirt" style="background:linear-gradient(160deg,#3a3a30,#a8c890 50%,#c8404a)"></div></div>
      <div class="calendar"><div class="weekdays"><span><b>Mo</b></span><span><b>Tu</b></span><span><b>We</b></span><span><b>Th</b></span><span><b>Fr</b></span><span><b>Sa</b></span><span><b>Su</b></span></div>
      <div class="days"><span class="out">31</span><span>1</span><span>2</span><span>3</span><span>4</span><span>5</span><span>6</span><span>7</span><span>8</span><span>9</span><span>10</span><span>11</span><span>12</span><span>13</span><span>14</span><span>15</span><span>16</span><span>17</span><span>18</span><span>19</span><span>20</span><span>21</span><span>22</span><span>23</span><span>24</span><span>25</span><span>26</span><span>27</span><span>28</span><span>29</span><span>30</span><span class="out">1</span><span class="out">2</span><span class="out">3</span><span class="out">4</span></div></div>
    </article>

    <article class="page m-oct">
      <h3 class="month-title"><span>October 2015</span></h3>
      <div class="photo collage-3"><div role="img" aria-label="October collage photo, baby sitting" style="background:linear-gradient(#5a4a40,#8a6a50)"></div><div role="img" aria-label="October collage photo, close-up" style="background:linear-gradient(#e0d8d0,#c8a898)"></div><div role="img" aria-label="October collage photo, baby with a football" style="background:linear-gradient(#6a5a4a,#e0e0e0)"></div></div>
      <div class="calendar"><div class="weekdays"><span><b>Mo</b></span><span><b>Tu</b></span><span><b>We</b></span><span><b>Th</b></span><span><b>Fr</b></span><span><b>Sa</b></span><span><b>Su</b></span></div>
      <div class="days"><span class="out">28</span><span class="out">29</span><span class="out">30</span><span>1</span><span>2</span><span>3</span><span>4</span><span>5</span><span>6</span><span>7</span><span>8</span><span>9</span><span>10</span><span>11</span><span>12</span><span>13</span><span>14</span><span>15</span><span>16</span><span>17</span><span>18</span><span>19</span><span>20</span><span>21</span><span>22</span><span>23</span><span>24</span><span>25</span><span>26</span><span>27</span><span>28</span><span>29</span><span>30</span><span>31</span><span class="out">1</span></div></div>
    </article>

    <article class="page m-nov">
      <h3 class="month-title"><span>November 2015</span></h3>
      <div class="photo"><div role="img" aria-label="November photo of the baby in a sun hat outdoors" style="background:linear-gradient(160deg,#3a6a30,#6a9048 45%,#d8c0b0 75%,#e8e8e8)"></div></div>
      <div class="calendar"><div class="weekdays"><span><b>Mo</b></span><span><b>Tu</b></span><span><b>We</b></span><span><b>Th</b></span><span><b>Fr</b></span><span><b>Sa</b></span><span><b>Su</b></span></div>
      <div class="days"><span class="out">26</span><span class="out">27</span><span class="out">28</span><span class="out">29</span><span class="out">30</span><span class="out">31</span><span>1</span><span>2</span><span>3</span><span>4</span><span>5</span><span>6</span><span>7</span><span>8</span><span>9</span><span>10</span><span>11</span><span>12</span><span>13</span><span>14</span><span>15</span><span>16</span><span>17</span><span>18</span><span>19</span><span>20</span><span>21</span><span>22</span><span>23</span><span>24</span><span>25</span><span>26</span><span>27</span><span>28</span><span>29</span><span>30</span><span class="out">1</span><span class="out">2</span><span class="out">3</span><span class="out">4</span><span class="out">5</span><span class="out">6</span></div></div>
    </article>

    <article class="page m-dec">
      <h3 class="month-title"><span>December 2015</span></h3>
      <div class="photo"><div role="img" aria-label="December photo" style="background:linear-gradient(120deg,#2f3a2a,#6a5a48 45%,#c9a070 70%,#d8d0c8)"></div></div>
      <div class="calendar"><div class="weekdays"><span><b>Mo</b></span><span><b>Tu</b></span><span><b>We</b></span><span><b>Th</b></span><span><b>Fr</b></span><span><b>Sa</b></span><span><b>Su</b></span></div>
      <div class="days"><span class="out">30</span><span>1</span><span>2</span><span>3</span><span>4</span><span>5</span><span>6</span><span>7</span><span>8</span><span>9</span><span>10</span><span>11</span><span>12</span><span>13</span><span>14</span><span>15</span><span>16</span><span>17</span><span>18</span><span>19</span><span>20</span><span>21</span><span>22</span><span>23</span><span>24</span><span>25</span><span>26</span><span>27</span><span>28</span><span>29</span><span>30</span><span>31</span><span class="out">1</span><span class="out">2</span><span class="out">3</span></div></div>
    </article>
  </section>

</main>
</body>
</html>
```